Window Cleaning Flyer targeting Shopfronts and Small Commercial Work

Single page flyer similar to the flyer targeting small commercial work and shopfronts

Please include the following text:

Brisk Pane Services delivers high quality service to suburbs all around Melbourne. From Frankston to Kalkallo, Brisk has you covered!

With over 10 years experience, Brisk specialises in providing:
- Window Cleaning: via elevated work platforms, rope access and extension poles
- Pressure Cleaning: Including chlorine treatment to prevent mould regrowth on concrete area
- Roof Gutter Cleaning: using our ladder free gutter vacuum

We pride ourselves on neat and professional presentation and vast geographical reach across Melbourne.

Our services can be completed on a frequency that meets your window cleaning needs. Whether a weekly clean or a yearly service.

Brisk Pane Services Melbourne takes care of all your window cleaning needs.

Contact Us now for free quote!

Target Market(s)

Small business and commercial building owners

Industry/Entity Type

Window Cleaning

Requirements
Must have
• Only use photos/logos provided
Should not have
• Stock phots

```html
<!DOCTYPE html>
<html lang="en">
<head>
<meta charset="utf-8">
<title>Brisk Pane Services – Window Cleaning Flyer</title>
<link href="https://fonts.googleapis.com/css2?family=PT+Sans:wght@400;700&family=PT+Sans+Narrow:wght@700&display=swap" rel="stylesheet">
<style>
  :root {
    --page-bg: #e4e4e4;
    --flyer-dark: #262626;
    --flyer-mid: #3a3a3a;
    --yellow: #ffe600;
    --blue: #174f7f;
    --red: #d9201c;
    --white: #ffffff;
    --panel: rgba(120,120,120,0.35);
    --sky-green: #6f8f4a;
    --brick: #8a4a34;
  }
  * { margin: 0; padding: 0; box-sizing: border-box; }
  html, body { width: 1200px; height: 750px; overflow: hidden; }
  body {
    background: var(--page-bg);
    font-family: "PT Sans", Arial, sans-serif;
    position: relative;
  }
  .flyer {
    position: absolute;
    left: 352px; top: 25px;
    width: 495px; height: 700px;
    background: linear-gradient(180deg, var(--flyer-dark) 0%, var(--flyer-mid) 55%, #2c2c2c 100%);
    overflow: hidden;
    color: var(--white);
  }
  .hero-photo {
    position: absolute;
    left: 205px; top: -95px;
    width: 400px; height: 400px;
    border-radius: 50%;
    border: 9px solid var(--blue);
    background: linear-gradient(135deg, var(--brick) 0%, #6d4a3e 35%, #7a7466 55%, var(--sky-green) 80%);
  }
  .detail-photo {
    position: absolute;
    left: 300px; top: 206px;
    width: 192px; height: 192px;
    border-radius: 50%;
    border: 7px solid var(--blue);
    background: linear-gradient(160deg, #c9a77a 0%, #b48f63 45%, #5f7e45 85%);
  }
  .brand {
    position: absolute;
    left: 22px; top: 30px;
    width: 200px;
    text-align: center;
    color: var(--yellow);
    font-weight: 700;
    font-size: 26px;
    line-height: 1.05;
    letter-spacing: 0.5px;
  }
  .headline {
    position: absolute;
    left: 22px; top: 120px;
    width: 200px;
    text-align: center;
    color: var(--yellow);
  }
  .headline-lead { font-size: 11px; font-weight: 700; letter-spacing: 0.5px; }
  .headline-main {
    font-family: "PT Sans Narrow", "Arial Narrow", sans-serif;
    font-size: 46px;
    line-height: 0.92;
    margin-top: 2px;
  }
  .headline-tail { font-size: 9px; font-weight: 700; text-align: right; padding-right: 18px; }
  .intro {
    position: absolute;
    left: 55px; top: 248px;
    width: 250px;
    text-align: center;
  }
  .intro-title { color: var(--yellow); font-weight: 700; font-size: 17px; }
  .intro-text { font-size: 11px; line-height: 1.3; margin-top: 2px; }
  .experience {
    position: absolute;
    left: 62px; top: 320px;
    width: 260px;
    font-size: 12.5px;
    font-weight: 700;
    line-height: 1.3;
  }
  .years-badge {
    display: inline-block;
    width: 24px; height: 24px;
    border-radius: 50%;
    background: var(--red);
    color: var(--yellow);
    text-align: center;
    line-height: 24px;
    font-size: 13px;
    vertical-align: middle;
    margin: 0 2px;
  }
  .service-list {
    position: absolute;
    left: 52px; top: 372px;
    width: 340px;
    list-style: none;
    font-size: 8.4px;
    line-height: 1.9;
  }
  .service-list li::before { content: "> "; color: var(--yellow); font-weight: 700; }
  .pride-panel {
    position: absolute;
    left: 40px; top: 440px;
    width: 262px; height: 130px;
    background: var(--panel);
    text-align: center;
    padding-top: 6px;
  }
  .pride-title { color: var(--yellow); font-weight: 700; font-size: 24px; line-height: 1; }
  .pride-lead { color: var(--yellow); font-weight: 700; font-size: 11px; line-height: 1.25; margin-top: 3px; }
  .pride-text { font-size: 10px; line-height: 1.25; margin-top: 8px; }
  .pride-text strong { color: var(--yellow); font-size: 11px; }
  .quote-burst {
    position: absolute;
    left: 300px; top: 440px;
    width: 150px; height: 150px;
  }
  .quote-burst svg { position: absolute; inset: 0; }
  .quote-text {
    position: absolute;
    inset: 0;
    display: flex; align-items: center; justify-content: center;
    text-align: center;
    color: var(--red);
    font-weight: 700;
    font-size: 19px;
    line-height: 1;
    transform: rotate(24deg);
  }
  .tagline {
    position: absolute;
    left: 60px; top: 584px;
    width: 380px;
    text-align: center;
    color: var(--yellow);
    font-weight: 700;
    font-size: 12px;
    letter-spacing: 0.6px;
    line-height: 1.2;
  }
  .contact-band {
    position: absolute;
    left: 0; top: 622px;
    width: 495px; height: 38px;
    background: var(--yellow);
    display: flex;
    font-size: 11px;
  }
  .contact-item { flex: 1; display: flex; align-items: center; justify-content: center; color: var(--red); }
  .contact-item + .contact-item { border-left: 2px solid var(--red); }
  .contact-label { font-weight: 700; font-size: 13px; margin-right: 4px; }
  .contact-item.phone span:last-child { color: #333; }
  .web-band {
    position: absolute;
    left: 0; top: 660px;
    width: 495px; height: 40px;
    background: var(--blue);
    text-align: center;
    line-height: 40px;
    font-size: 14px;
  }
</style>
</head>
<body>
  <main class="flyer">
    <div class="hero-photo" role="img" aria-label="Photo of a technician on an elevated work platform cleaning the windows of a brick building"></div>
    <div class="detail-photo" role="img" aria-label="Photo of a cleaner using an extension pole on windows behind timber louvres"></div>

    <div class="brand">BRISK PANE<br>SERVICES</div>

    <div class="headline">
      <div class="headline-lead">TAKES CARE OF ALL YOUR</div>
      <div class="headline-main">WINDOW<br>CLEANING</div>
      <div class="headline-tail">NEEDS.</div>
    </div>

    <section class="intro">
      <h2 class="intro-title">BRISK PANE SERVICES</h2>
      <p class="intro-text">delivers high quality service to suburbs<br>all around Melbourne. From Frankston<br>to Kalkallo, Brisk has you covered!</p>
    </section>

    <p class="experience">With over <span class="years-badge">10</span> years experience, Brisk<br>specialises in providing:</p>

    <ul class="service-list">
      <li>Window Cleaning: via elevated work platforms, rope access and extension poles</li>
      <li>Pressure Cleaning: Including chlorine treatment to prevent mould regrowth on concrete area</li>
      <li>Roof Gutter Cleaning: using our ladder free gutter vacuum</li>
    </ul>

    <section class="pride-panel">
      <h3 class="pride-title">WE PRIDE</h3>
      <p class="pride-lead">ourselves on neat and professional presentation<br>and vast geographical reach across Melbourne.</p>
      <p class="pride-text">Our services can be completed on a<br>frequency that meets your window cleaning needs.<br><strong>Whether a weekly clean or a yearly service.</strong></p>
    </section>

    <div class="quote-burst">
      <svg viewBox="0 0 150 150" width="150" height="150" aria-hidden="true">
        <polygon fill="#ffe600" points="149,75 135.8,87.1 143.4,103.3 126.5,109.5 127.3,127.3 109.5,126.5 103.3,143.4 87.1,135.8 75,149 62.9,135.8 46.7,143.4 40.5,126.5 22.7,127.3 23.5,109.5 6.6,103.3 14.2,87.1 1,75 14.2,62.9 6.6,46.7 23.5,40.5 22.7,22.7 40.5,23.5 46.7,6.6 62.9,14.2 75,1 87.1,14.2 103.3,6.6 109.5,23.5 127.3,22.7 126.5,40.5 143.4,46.7 135.8,62.9"/>
      </svg>
      <div class="quote-text">Contact Us<br>now for<br>free quote!</div>
    </div>

    <p class="tagline">Brisk Pane Services Melbourne<br>takes care of all your window cleaning needs.</p>

    <div class="contact-band">
      <div class="contact-item phone"><span class="contact-label">Tel:</span><span>000 111 2222</span></div>
      <div class="contact-item email"><span class="contact-label">Email:</span><span>youremail@here.com</span></div>
    </div>
    <div class="web-band">www.yourwebsitehere.com</div>
  </main>
</body>
</html>
```